Business Card Design Project

We need a double-sided business card design for our e-commerce company. Be as creative as you can.

Reason: Change of logo

Target Market(s)

Business owners

Industry/Entity Type

E-Commerce

Requirements
Must have
• Name (editable)
Mobile number -editable
www.trizvo.com - MUST STAND OUT ALONE
Office address:
27 Pellow Road
#09-04 Corbell Tower
Singapore 058214

```html
<!DOCTYPE html>
<html lang="en">
<head>
<meta charset="utf-8">
<title>Trizvo Business Card</title>
<link href="https://fonts.googleapis.com/css2?family=Nunito+Sans:ital,wght@0,400;0,700;0,800;1,400&display=swap" rel="stylesheet">
<style>
  :root {
    --bg: #e9e9ec;
    --card: #ffffff;
    --blue: #1565c0;
    --blue-block: #1a73d1;
    --wave-dark: #0f7fcf;
    --wave-light: #8fd0f3;
    --orange: #f47a24;
    --ink: #1d1d1d;
    --white: #ffffff;
  }
  * { margin: 0; padding: 0; box-sizing: border-box; }
  html, body { width: 1200px; height: 900px; overflow: hidden; }
  body {
    background: var(--bg);
    font-family: "Nunito Sans", Arial, sans-serif;
    color: var(--ink);
    position: relative;
  }
  .card {
    position: absolute;
    left: 340px;
    width: 520px;
    height: 298px;
    background: var(--card);
    border-radius: 16px;
    overflow: hidden;
    box-shadow: 0 10px 28px rgba(0,0,0,0.18);
  }
  .card--front { top: 110px; }
  .card--back { top: 480px; }

  /* Front */
  .brand {
    position: absolute;
    left: 44px;
    top: 92px;
  }
  .brand__name {
    font-size: 64px;
    font-weight: 800;
    color: var(--blue);
    line-height: 1;
    letter-spacing: 1px;
  }
  .brand__tagline {
    margin-top: 12px;
    font-size: 13px;
    letter-spacing: 4px;
    text-transform: uppercase;
    color: var(--ink);
  }
  .front-block {
    position: absolute;
    right: 34px;
    top: 62px;
    width: 160px;
    height: 170px;
    background: var(--orange);
    border-radius: 4px;
  }

  /* Back */
  .back-block {
    position: absolute;
    left: 44px;
    top: 44px;
    width: 200px;
    height: 180px;
    background: var(--blue-block);
    border-radius: 3px;
  }
  .wave {
    position: absolute;
    left: 0;
    bottom: 0;
    width: 520px;
    height: 90px;
  }
  .web {
    position: absolute;
    left: 0;
    right: 0;
    bottom: 14px;
    text-align: center;
    font-size: 20px;
    letter-spacing: 8px;
    color: var(--white);
    font-weight: 700;
  }
  .contact {
    position: absolute;
    left: 282px;
    top: 50px;
  }
  .contact__name {
    font-size: 18px;
    font-weight: 800;
    color: var(--blue);
    text-transform: uppercase;
    letter-spacing: 0.5px;
  }
  .contact__role {
    font-size: 13px;
    font-style: italic;
    color: var(--blue);
    margin-bottom: 16px;
  }
  .contact__line {
    display: flex;
    align-items: center;
    gap: 7px;
    font-size: 14px;
    line-height: 1.5;
  }
  .contact__line svg { width: 13px; height: 13px; flex: none; }
  .address {
    margin-top: 14px;
    font-size: 12px;
    text-transform: uppercase;
    line-height: 1.5;
    letter-spacing: 0.3px;
  }
</style>
</head>
<body>
  <section class="card card--front">
    <div class="brand">
      <div class="brand__name">Trizvo</div>
      <div class="brand__tagline">Happy Shoppers Unite!</div>
    </div>
    <div class="front-block"></div>
  </section>

  <section class="card card--back">
    <div class="back-block"></div>
    <svg class="wave" viewBox="0 0 520 90" preserveAspectRatio="none">
      <path d="M0 30 C 140 50, 300 70, 520 52 L520 90 L0 90 Z" fill="var(--wave-dark)"/>
      <path d="M0 24 C 140 44, 300 62, 520 44 L520 52 C 300 70, 140 50, 0 30 Z" fill="var(--wave-light)"/>
    </svg>
    <div class="web">www.trizvo.com</div>

    <div class="contact">
      <div class="contact__name">Alan Tan</div>
      <div class="contact__role">Director</div>
      <div class="contact__line">
        <svg viewBox="0 0 14 14"><circle cx="7" cy="7" r="7" fill="#1565c0"/><rect x="4.5" y="2.8" width="5" height="8.4" rx="1" fill="#fff"/><rect x="5.4" y="3.8" width="3.2" height="5" fill="#1565c0"/></svg>
        <span>0198 765 432</span>
      </div>
      <div class="contact__line">
        <svg viewBox="0 0 14 14"><circle cx="7" cy="7" r="7" fill="#1565c0"/><rect x="3" y="4.2" width="8" height="5.6" fill="#fff"/><path d="M3 4.2 L7 7.4 L11 4.2" stroke="#1565c0" stroke-width="0.9" fill="none"/></svg>
        <span>alantan@trizvo.com</span>
      </div>
      <div class="address">
        27 Pellow Road<br>
        #09-04 Corbell Tower<br>
        Singapore 058214
      </div>
    </div>
  </section>
</body>
</html>
```